FRONT BUS CARD:

We were maybe thinking to have the text in a "common seal" which is an oval shape. Or CROWN VAULT underlined, then AUSTRALIA underneath...

Picture to have in the seal, or next to the words if seal not used: Gold Bars (3 of them), or scales of justice..

LOGO and pic and font to be in shiny gold.
We want 1 black background design and 1 white background design.

CROWN VAULT TRADERS

```html
<!DOCTYPE html>
<html lang="en">
<head>
<meta charset="utf-8">
<title>Crown Vault Traders – Business Cards</title>
<link rel="stylesheet" href="https://fonts.googleapis.com/css2?family=Montserrat:wght@400;500;800&display=swap">
<style>
  :root {
    --stage: #3b3b3d;
    --card-black: #000000;
    --gold-deep: #a8761f;
    --gold-mid: #d4a53a;
    --gold-light: #f6e08c;
    --gold-pale: #f3dc86;
    --gold-text: #d6aa3e;
    --ink: #1a1408;
    --ink-soft: #5a4a25;
  }
  * { box-sizing: border-box; margin: 0; padding: 0; }
  html, body {
    width: 1200px;
    height: 534px;
    overflow: hidden;
  }
  body {
    position: relative;
    background: var(--stage);
    font-family: "Montserrat", sans-serif;
  }
  .card {
    position: absolute;
    top: 118px;
    width: 523px;
    height: 300px;
    border-radius: 20px;
    border: 3px solid transparent;
    background:
      linear-gradient(var(--card-black), var(--card-black)) padding-box,
      linear-gradient(135deg, var(--gold-light), var(--gold-deep) 40%, var(--gold-light) 70%, var(--gold-mid)) border-box;
    overflow: hidden;
  }
  .card--front { left: 63px; }
  .card--back { left: 622px; }

  .gold-band {
    position: absolute;
    left: 0;
    right: 0;
    bottom: 0;
    background: linear-gradient(90deg,
      var(--gold-mid) 0%, var(--gold-light) 12%, var(--gold-deep) 30%,
      var(--gold-light) 48%, var(--gold-mid) 62%, var(--gold-pale) 80%,
      var(--gold-deep) 92%, var(--gold-light) 100%);
  }
  .card--front .gold-band { height: 39px; }
  .card--back .gold-band { height: 108px; }

  .wordmark {
    position: absolute;
    left: 0;
    right: 0;
    text-align: center;
    color: var(--gold-text);
    font-weight: 800;
    line-height: 1;
  }
  .wordmark span { display: block; }
  .card--front .wordmark { top: 66px; }
  .card--front .wordmark__line1 { font-size: 60px; letter-spacing: 2px; }
  .card--front .wordmark__line2 { font-size: 60px; letter-spacing: 2px; margin-top: 2px; }
  .card--front .wordmark__line3 { font-size: 15px; letter-spacing: 5px; margin-top: 6px; }

  .card--back .wordmark { top: 40px; }
  .card--back .wordmark__line1 { font-size: 46px; letter-spacing: 2px; }
  .card--back .wordmark__line2 { font-size: 46px; letter-spacing: 2px; margin-top: 3px; }
  .card--back .wordmark__line3 { font-size: 12px; letter-spacing: 4px; margin-top: 7px; }

  .contact {
    position: absolute;
    left: 84px;
    top: 214px;
    color: var(--ink);
  }
  .contact__name {
    font-size: 17px;
    font-weight: 500;
  }
  .contact__role {
    font-size: 11px;
    color: var(--ink-soft);
    margin-left: 6px;
    font-weight: 400;
  }
  .contact__grid {
    display: grid;
    grid-template-columns: 131px auto;
    row-gap: 3px;
    margin-top: 8px;
    font-size: 12px;
    font-weight: 400;
  }
</style>
</head>
<body>
  <section class="card card--front" aria-label="Card front">
    <h1 class="wordmark">
      <span class="wordmark__line1">CROWN</span>
      <span class="wordmark__line2">VAULT</span>
      <span class="wordmark__line3">TRADERS</span>
    </h1>
    <div class="gold-band"></div>
  </section>

  <section class="card card--back" aria-label="Card back">
    <h2 class="wordmark">
      <span class="wordmark__line1">CROWN</span>
      <span class="wordmark__line2">VAULT</span>
      <span class="wordmark__line3">TRADERS</span>
    </h2>
    <div class="gold-band"></div>
    <div class="contact">
      <p class="contact__name">Alex Reed<span class="contact__role">Position</span></p>
      <div class="contact__grid">
        <span>tel: 0000 222 8000</span>
        <span>email: info@crownvaulttraders.co.au</span>
        <span>fax: 0222 222 0000</span>
        <span>web: www.crownvaulttraders.co.au</span>
      </div>
    </div>
  </section>
</body>
</html>
```